metal roofing website

I have several domain names and a website that has been built. I need someone to recreate essentially the same website and change some photos and basic design to create the new sites. I have all of the files and c panel access to the lucky winner. If you can do a good job at a fair price I will have 100's of sites to send to you very soon. I have the site built and have all files just need it recreated on my server. the current site is www.brantlepanelinc.com I am looking to get this done ASAP!!!

```html
<!DOCTYPE html>
<html lang="en">
<head>
<meta charset="utf-8">
<title>Brantle Panel Inc — Building Components</title>
<link rel="stylesheet" href="https://fonts.googleapis.com/css2?family=Montserrat:wght@400;500;600;700&family=Roboto:wght@300;400;500&family=Lora:ital@1&family=Josefin+Sans:wght@400&display=swap">
<style>
:root{
  --red:#c0261c;
  --red-band:#b3302a;
  --red-deep:#a5121a;
  --red-dark:#6a0e10;
  --beige:#e4d6c2;
  --topbar:#f3f3f3;
  --ink:#222222;
  --muted:#8a8a8a;
  --line:#dcdcdc;
  --light:#f2f2f2;
  --footer:#1b1b1b;
  --footer-text:#9b9b9b;
  --white:#ffffff;
  --dark-btn:#4a4a4a;
}
*{margin:0;padding:0;box-sizing:border-box}
html,body{width:1200px;height:2268px;overflow:hidden}
body{position:relative;background:var(--white);font-family:"Roboto",sans-serif;color:var(--ink)}
.abs{position:absolute}
.topbar{left:0;top:0;width:1200px;height:26px;background:var(--topbar);font-family:"Montserrat",sans-serif;font-size:10px;color:#777}
.topbar .tagline{left:236px;top:7px}
.topbar .links{right:244px;top:7px;display:flex;gap:14px;align-items:center}
.dot{width:8px;height:8px;border-radius:50%;background:#777;display:inline-block}
.header{left:0;top:26px;width:1200px;height:87px;background:var(--beige)}
.brand{left:236px;top:28px;display:flex;align-items:center;gap:8px;font-family:"Montserrat",sans-serif;font-weight:700;font-size:18px;color:var(--red)}
.brand .sq{width:14px;height:14px;background:var(--red)}
.nav{left:617px;top:37px;display:flex;gap:10px;font-family:"Montserrat",sans-serif;font-size:11.5px;color:#5a2a22}
.nav .active{color:var(--red)}
.nav .sep{color:#9a8a7a}
.hero{left:0;top:113px;width:1200px;height:373px;background:linear-gradient(180deg,#7f8e86 0%,#a9ad9d 45%,#7c8450 78%,#4f6a2c 100%)}
.hero-box{left:242px;top:238px;width:268px;height:148px;background:rgba(30,30,30,.85);padding:18px 12px}
.hero-box .kicker{font-family:"Montserrat",sans-serif;font-size:9.5px;color:#fff;font-weight:500}
.hero-box h1{font-family:"Montserrat",sans-serif;font-size:19px;line-height:24px;color:#fff;font-weight:700;margin-top:14px;letter-spacing:.3px}
.btn{display:inline-block;font-family:"Montserrat",sans-serif;font-size:9.5px;font-weight:600;color:#fff;text-align:center}
.hero-box .see{left:12px;top:108px;width:111px;height:28px;line-height:28px;background:var(--red)}
.hero-box .quote{left:132px;top:108px;width:118px;height:28px;line-height:26px;border:1px solid var(--red)}
.cta-band{left:0;top:486px;width:1200px;height:62px;background:var(--red-band)}
.cta-band p{position:absolute;left:242px;top:18px;font-family:"Lora",serif;font-style:italic;font-size:19px;color:#fff}
.cta-band .btn{position:absolute;left:825px;top:16px;width:116px;height:32px;line-height:32px;background:#6f0f12;font-size:9px}
.section-title{font-family:"Montserrat",sans-serif;font-weight:600;font-size:15.5px;color:var(--red);letter-spacing:.5px}
.rule{height:1px;background:var(--line)}
.small{font-size:10px;line-height:16px;color:var(--muted)}
.arrow{width:24px;height:24px;display:flex;align-items:center;justify-content:center}
.arrow.red{background:var(--red)}
.arrow.gray{background:var(--dark-btn)}
.card-title{font-family:"Montserrat",sans-serif;font-size:11.5px;font-weight:600;color:var(--red)}
.readmore{font-family:"Montserrat",sans-serif;font-size:8.5px;color:#555;border-bottom:1px solid #555;padding-bottom:2px}
.photo{border-radius:0}
.projects{left:0;top:885px;width:1200px;height:359px;background:var(--light)}
.tabs{left:462px;top:970px;display:flex;gap:22px;font-family:"Montserrat",sans-serif;font-size:11px;color:#333}
.tabs .on{color:var(--red);border-bottom:2px solid var(--red);padding-bottom:4px}
.consult{left:728px;top:1289px;width:224px;height:89px;background:linear-gradient(135deg,#5b5b5b,#2e2e2e);color:#fff;font-family:"Roboto",sans-serif;text-align:center;padding-top:16px}
.consult .a{font-size:11px;font-weight:500}
.consult .b{font-size:15px;margin-top:3px}
.consult .c{font-size:8px;margin-top:6px;display:inline-block;border-bottom:1px solid #fff}
.promise{left:0;top:1508px;width:1200px;height:164px;background:linear-gradient(120deg,var(--red-deep),#8d0f14 60%,var(--red-deep));text-align:center;color:#fff}
.promise p{font-family:"Josefin Sans",sans-serif;font-size:16px;line-height:21px;margin-top:40px;letter-spacing:.5px}
.promise .call{font-family:"Montserrat",sans-serif;font-weight:600;font-size:15px;margin-top:30px}
.testimonials{left:0;top:1672px;width:1200px;height:330px;background:var(--light)}
.quote-card{width:346px;height:109px;background:#fff;padding:20px 20px 0 68px;font-size:10.5px;line-height:18px;font-style:italic;color:#777}
.quote-mark{left:20px;top:20px;font-family:"Lora",serif;font-size:48px;line-height:40px;color:#ccc;font-style:normal}
.avatar{width:56px;height:56px;border-radius:50%;background:linear-gradient(#c9b6a4,#8a735f)}
.person .name{font-family:"Roboto",sans-serif;font-size:12px;color:#333}
.person .role{font-size:9px;color:#888;margin-top:4px}
.footer{left:0;top:2002px;width:1200px;height:233px;background:var(--footer);color:var(--footer-text);font-size:10px}
.footer h3{font-family:"Montserrat",sans-serif;font-size:13px;font-weight:500;color:#bbb}
.footer .f-brand{font-family:"Montserrat",sans-serif;font-weight:700;font-size:17px;color:var(--red)}
.footer ul{list-style:none}
.footer li{height:23px}
.copy{left:0;top:2235px;width:1200px;height:33px;background:var(--red-dark);color:#ddd;font-size:9px;text-align:center;line-height:33px}
</style>
</head>
<body>

<div class="abs topbar">
  <span class="abs tagline">We are the manufacturer of building components</span>
  <div class="abs links"><span>Carrier</span><span>Give Feedback</span><span>Contact</span><span class="dot"></span><span class="dot"></span><span class="dot"></span></div>
</div>

<header class="abs header">
  <div class="abs brand"><span class="sq"></span>BRANTLE PANEL</div>
  <nav class="abs nav">
    <span class="active">Home</span><span class="sep">-</span><span>About Us</span><span class="sep">-</span><span>Services &#8964;</span><span class="sep">-</span><span>Gallery</span><span class="sep">-</span><span>Contact Us</span>
  </nav>
</header>

<section class="abs hero" role="img" aria-label="Photo of a large beige post frame barn with dormers and a covered porch on green lawn"></section>
<div class="abs hero-box">
  <div class="kicker">WE ARE BRINGING BEST ROOFING SOLUTIONS</div>
  <h1>COMPLETE POST FRAME AND GARAGES</h1>
  <span class="abs btn see">SEE MORE</span>
  <span class="abs btn quote">GET A FREE QUOTE</span>
</div>

<div class="abs cta-band">
  <p>Looking for a quality building component supplier for your project?</p>
  <span class="btn">GET A FREE QUOTE</span>
</div>

<!-- Services -->
<h2 class="abs section-title" style="left:242px;top:584px">OUR SERVICES</h2>
<div class="abs rule" style="left:242px;top:610px;width:226px"></div>
<p class="abs small" style="left:242px;top:624px;width:224px">Our projects may be diverse but the results are one and the same—on schedule, on budget, with superior quality and safe. It's a certainty you can count on.</p>
<div class="abs arrow red" style="left:245px;top:685px"><svg width="8" height="8" viewBox="0 0 8 8"><path d="M5 1L2 4l3 3" stroke="#fff" fill="none"/></svg></div>
<div class="abs arrow gray" style="left:277px;top:685px"><svg width="8" height="8" viewBox="0 0 8 8"><path d="M3 1l3 3-3 3" stroke="#fff" fill="none"/></svg></div>

<div class="abs photo" role="img" aria-label="Photo of a grey post frame building with white roll-up door" style="left:487px;top:580px;width:226px;height:124px;background:linear-gradient(180deg,#8fb0d4 0%,#b9c8d6 45%,#7e7f80 60%,#9a9488 100%)"></div>
<h3 class="abs card-title" style="left:488px;top:714px">Complete Post frame Building Packages</h3>
<p class="abs small" style="left:488px;top:738px;width:226px">Depending on the scope of your project, we design your renovation in-house or partner with Builder's finest architects to design, budget and build.</p>
<span class="abs readmore" style="left:488px;top:790px">READ MORE</span>

<div class="abs photo" role="img" aria-label="Photo of a red residential garage with dark metal roof among trees" style="left:732px;top:580px;width:224px;height:124px;background:linear-gradient(180deg,#8ea1b3 0%,#4f4a44 40%,#8b2f24 70%,#8c8f7e 100%)"></div>
<h3 class="abs card-title" style="left:736px;top:716px">Residential Metal Roofing</h3>
<p class="abs small" style="left:733px;top:738px;width:224px">Integrity for what we build, the purpose of why we build. We build a house with the synchronism between design and build package.</p>
<span class="abs readmore" style="left:733px;top:790px">READ MORE</span>

<!-- Projects -->
<section class="abs projects">
  <div class="abs" style="right:2px;top:0;width:3px;height:359px;background:var(--red)"></div>
</section>
<h2 class="abs section-title" style="left:242px;top:910px">LATEST PROJECTS</h2>
<div class="abs rule" style="left:242px;top:934px;width:714px;background:#cfcfcf"></div>
<div class="abs arrow red" style="left:903px;top:905px"><svg width="8" height="8" viewBox="0 0 8 8"><path d="M5 1L2 4l3 3" stroke="#fff" fill="none"/></svg></div>
<div class="abs arrow gray" style="left:935px;top:905px"><svg width="8" height="8" viewBox="0 0 8 8"><path d="M3 1l3 3-3 3" stroke="#fff" fill="none"/></svg></div>
<div class="abs tabs"><span class="on">All</span><span>Residential</span><span>Commecial</span><span>Aggricultural</span></div>
<div class="abs" role="img" aria-label="Photo of a tan barn with red roof and cupola" style="left:242px;top:1014px;width:176px;height:192px;background:linear-gradient(180deg,#9fb3c9 0%,#c9b99a 45%,#b79a74 75%,#6f7a4a 100%)"></div>
<div class="abs" role="img" aria-label="Photo of a blue shed with salmon double doors" style="left:422px;top:1014px;width:176px;height:192px;background:linear-gradient(180deg,#f0f0f0 0%,#2d6f86 30%,#d98f7e 65%,#8c8c8c 100%)"></div>
<div class="abs" role="img" aria-label="Photo of a raised wooden hunting stand in snow" style="left:602px;top:1014px;width:176px;height:192px;background:linear-gradient(180deg,#7fa3cc 0%,#9a7a5c 45%,#b09070 65%,#e8ecef 100%)"></div>
<div class="abs" role="img" aria-label="Photo of a tan portable shed with dark roof and windows" style="left:782px;top:1014px;width:174px;height:192px;background:linear-gradient(180deg,#ffffff 0%,#3f2f3a 25%,#d8c39a 55%,#6f9a4a 100%)"></div>

<!-- What we are -->
<div class="abs" role="img" aria-label="Photo of three professionals in suits and white hard hats" style="left:242px;top:1289px;width:224px;height:145px;background:linear-gradient(135deg,#9a9a9a,#3a3a3a 60%,#222)"></div>
<h2 class="abs" style="left:484px;top:1293px;font-family:'Roboto',sans-serif;font-weight:400;font-size:16px;color:#222">What We Are?</h2>
<div class="abs rule" style="left:484px;top:1318px;width:226px"></div>
<p class="abs small" style="left:484px;top:1334px;width:226px">Builder wants to be your builder for life. Whether we built your home or not, it's not too late for you to join our family. BuildCore is managed by a staff with over 30 years of renovation experience and supported by the same systems.</p>
<span class="abs readmore" style="left:484px;top:1423px">READ MORE</span>

<div class="abs consult" role="img" aria-label="Darkened photo of builders reviewing plans">
  <div class="a">GET YOUR</div>
  <div class="b">FREE CONSULTING</div>
  <span class="c">CLICK HERE!</span>
</div>
<p class="abs small" style="left:728px;top:1390px;width:226px">If you are confusing? Do not worry. We offer free consultation to help you make a decision with the best creativity and quality that you deserve.</p>

<!-- Promise -->
<section class="abs promise">
  <p>Our promise as a contractor is to build community value into every project while delivering<br>professional expertise, exceptional customers service and quality construction.</p>
  <div class="call">Call Us : 555-210-0765 &nbsp;&nbsp;&nbsp;&nbsp;&nbsp;|&nbsp;&nbsp;&nbsp;&nbsp;&nbsp; Fax : 555-210-0994</div>
</section>

<!-- Testimonials -->
<section class="abs testimonials"></section>
<h2 class="abs" style="left:242px;top:1707px;font-family:'Roboto',sans-serif;font-weight:400;font-size:16px;color:#222">Testimonials</h2>
<div class="abs quote-card" style="left:242px;top:1760px">
  <span class="abs quote-mark">&#8220;</span>
  "Builder has an exceptional track record building on the Riverside State campus, and we were confident in their ability to work collaboratively to ensure that a project of this magnitude was delivered successfully."
</div>
<svg class="abs" style="left:262px;top:1868px" width="16" height="9"><path d="M0 0h16L0 9z" fill="#fff"/></svg>
<div class="abs quote-card" style="left:607px;top:1760px">
  <span class="abs quote-mark">&#8220;</span>
  "We have assembled a project team comprised of the nation's top laboratory design and building professionals and are delighted to have Builder execute our vision for this unprecedented facility."
</div>
<svg class="abs" style="left:627px;top:1868px" width="16" height="9"><path d="M0 0h16L0 9z" fill="#fff"/></svg>
<div class="abs avatar" role="img" aria-label="Portrait of Clara Wendell" style="left:245px;top:1887px"></div>
<div class="abs person" style="left:310px;top:1903px"><div class="name">Ms. Clara Wendell</div><div class="role">Founder/ CEO of Builder Ltd.</div></div>
<div class="abs avatar" role="img" aria-label="Portrait of Martin Osei" style="left:608px;top:1887px"></div>
<div class="abs person" style="left:675px;top:1903px"><div class="name">Mr. Martin Osei</div><div class="role">Founder/ CEO of Northgate Works</div></div>

<!-- Footer -->
<footer class="abs footer">
  <div class="abs f-brand" style="left:239px;top:40px">BRANTLE PANEL INC</div>
  <p class="abs" style="left:241px;top:81px;width:224px;line-height:19px">Integrity for what we build, the purpose of why we build and the people who inspire us to build. It's what Builder is built upon, and why our homes are as far from ordinary as the people who live in them.</p>
  <div class="abs" style="left:241px;top:188px;display:flex;gap:18px"><span class="dot" style="background:#ddd"></span><span class="dot" style="background:#ddd"></span><span class="dot" style="background:#ddd"></span></div>

  <h3 class="abs" style="left:487px;top:44px">Information</h3>
  <div class="abs rule" style="left:487px;top:66px;width:224px;background:#3a3a3a"></div>
  <ul class="abs" style="left:489px;top:78px"><li>About Us</li><li>Our Team</li><li>Testimonials</li><li>Services</li><li>Careers</li></ul>
  <ul class="abs" style="left:616px;top:76px"><li>Overview</li><li>Renovation</li><li>Who We Are</li><li>Projects</li><li>Careers</li></ul>

  <h3 class="abs" style="left:734px;top:44px">Contact Info</h3>
  <div class="abs rule" style="left:734px;top:66px;width:184px;background:#3a3a3a"></div>
  <ul class="abs" style="left:746px;top:76px"><li>28 Harrow Lane, Millbrook, England</li><li>555-210-0765</li><li>info@brantlepanel.com</li><li>555-210-0994</li><li>Mon - Sat: 9:00 - 18:00</li></ul>
</footer>
<div class="abs copy">© 2019, All Rights Reserved, BrantlePanel, Inc</div>

</body>
</html>
```